Meisterbetrieb für Trockenbau & Sanierungsarbeiten etc. benötigt Fahrzeugbeschriftung
Zielgruppe
KALMORANBAU
Wir sind ein Stuckateur Meisterbetrieb für Trockenbau, Innenputz, Außenputz, Malerarbeiten, Akustikdecken, Sanierungsarbeiten für Innen- und Außenfassaden, Altbausanierungen, Innenausbau.
Zielgruppe: Privatpersonen, Gewerbebetriebe/Unternehmen, Öffentliche Einrichtungen, Bauträger
Aufgabenstellung
1) Logo sollte auf jeder Seite gut sichtbar sein
2) Wir wollen mit dem Fahrzeug auffallen
3) Im Hintergrund dürfen gerne Fotos verwendet werden (Auch Bildrux oder dergleichen, falls bei uns nichts dabei)
4) Der Kreativität sind keine Grenzen gesetzt (Rot ist die Hauptfarbe)
Bitte die wichtigsten Kontaktdaten (Handynummer, E-Mail Adresse, Internetseite) sollten enthalten sein.
Fahrzeug
Bedruckt sollen alle Seiten werden (Vorne, Hinten, Links, Rechts, Dach)

```html
<!DOCTYPE html>
<html lang="de">
<head>
<meta charset="utf-8">
<title>KALMORANBAU – Fahrzeugbeschriftung</title>
<link rel="stylesheet" href="https://fonts.googleapis.com/css2?family=Josefin+Sans:wght@400;600&family=Open+Sans:wght@600;700&display=swap">
<style>
  :root {
    --wrap-red: #e21f26;
    --wrap-grey: #48484a;
    --wrap-black: #2a2a2b;
    --wrap-white: #ffffff;
    --panel-edge: #d9d9d9;
    --page-bg: #f2f2f2;
  }
  html, body {
    margin: 0;
    width: 1200px;
    height: 1190px;
    overflow: hidden;
    background: var(--page-bg);
  }
  .wrap-sheet { display: block; width: 1200px; height: 1190px; }
  .wordmark {
    font-family: "Josefin Sans", sans-serif;
    font-weight: 600;
    fill: var(--wrap-grey);
  }
  .master-line {
    font-family: "Open Sans", sans-serif;
    font-weight: 600;
    fill: var(--wrap-red);
  }
  .claim {
    font-family: "Josefin Sans", sans-serif;
    font-weight: 400;
    fill: var(--wrap-grey);
  }
  .contact {
    font-family: "Open Sans", sans-serif;
    font-weight: 700;
    fill: var(--wrap-white);
  }
  .panel { fill: var(--wrap-white); stroke: var(--panel-edge); stroke-width: 2; }
  .band-grey { fill: var(--wrap-grey); }
  .band-red { fill: var(--wrap-red); }
  .band-black { fill: var(--wrap-black); }
  .divider { stroke: var(--wrap-grey); stroke-width: 1.5; }
  .mark-square { fill: var(--wrap-red); }
</style>
</head>
<body>
<svg class="wrap-sheet" viewBox="0 0 1200 1190" xmlns="http://www.w3.org/2000/svg">
  <defs>
    <clipPath id="side-clip"><rect x="30" y="20" width="1140" height="500" rx="40"/></clipPath>
    <clipPath id="rear-clip"><rect x="680" y="565" width="490" height="600" rx="30"/></clipPath>
  </defs>

  <!-- Side view -->
  <g class="side-wrap">
    <rect class="panel" x="30" y="20" width="1140" height="500" rx="40"/>
    <g clip-path="url(#side-clip)">
      <polygon class="band-grey" points="30,400 1170,200 1170,252 30,460"/>
      <polygon class="band-grey" points="30,400 400,336 400,430 30,430"/>
      <polygon class="band-red" points="395,381 1170,255 1170,400 395,400"/>
      <polygon fill="#ffffff" points="395,378 1170,250 1170,256 395,384"/>
      <rect class="band-black" x="30" y="395" width="1140" height="125"/>
      <rect class="band-red" x="320" y="425" width="500" height="22"/>
    </g>
    <g class="side-lockup" transform="rotate(-9 760 175)">
      <rect class="mark-square" x="730" y="35" width="58" height="58"/>
      <text class="wordmark" x="760" y="170" font-size="46" letter-spacing="11" text-anchor="middle">KALMORANBAU</text>
      <line class="divider" x1="515" y1="197" x2="570" y2="197"/>
      <line class="divider" x1="950" y1="197" x2="1005" y2="197"/>
      <text class="master-line" x="760" y="203" font-size="22" text-anchor="middle">Stuckateurmeister Hauke Brendel</text>
      <text class="claim" x="760" y="237" font-size="21" letter-spacing="9" text-anchor="middle">MIT HANDWERK ZUM ZUHAUSE</text>
    </g>
    <text class="contact" x="525" y="352" font-size="34" transform="rotate(-9 525 352)">0171/20XX5XX</text>
    <text class="contact" x="660" y="378" font-size="25" transform="rotate(-9 660 378)">www.kalmoranbau-brendel.de</text>
  </g>

  <!-- Front view -->
  <g class="front-wrap">
    <rect class="panel" x="30" y="565" width="620" height="600" rx="30"/>
    <rect class="mark-square" x="315" y="585" width="50" height="50"/>
    <rect x="110" y="650" width="460" height="120" rx="16" fill="#e9e9ea"/>
    <text class="wordmark" x="340" y="818" font-size="22" letter-spacing="6" text-anchor="middle">KALMORANBAU</text>
    <line class="divider" x1="172" y1="826" x2="205" y2="826"/>
    <line class="divider" x1="475" y1="826" x2="508" y2="826"/>
    <text class="master-line" x="340" y="830" font-size="11" text-anchor="middle">Stuckateurmeister Hauke Brendel</text>
    <text class="claim" x="340" y="846" font-size="10" letter-spacing="5" text-anchor="middle">MIT HANDWERK ZUM ZUHAUSE</text>
    <rect class="band-black" x="30" y="1040" width="620" height="125" opacity="0.15"/>
  </g>

  <!-- Rear view -->
  <g class="rear-wrap">
    <rect class="panel" x="680" y="565" width="490" height="600" rx="30"/>
    <g clip-path="url(#rear-clip)">
      <rect class="band-grey" x="680" y="780" width="490" height="58"/>
      <rect fill="#ffffff" x="680" y="838" width="490" height="4"/>
      <rect class="band-red" x="680" y="842" width="490" height="150"/>
      <rect class="band-black" x="680" y="992" width="490" height="173"/>
      <line x1="925" y1="565" x2="925" y2="1165" stroke="#bdbdbd" stroke-width="1.5" opacity="0.6"/>
    </g>
    <rect class="mark-square" x="893" y="625" width="64" height="64"/>
    <text class="wordmark" x="925" y="724" font-size="28" letter-spacing="7" text-anchor="middle">KALMORANBAU</text>
    <line class="divider" x1="752" y1="737" x2="795" y2="737"/>
    <line class="divider" x1="1055" y1="737" x2="1098" y2="737"/>
    <text class="master-line" x="925" y="742" font-size="14" text-anchor="middle">Stuckateurmeister Hauke Brendel</text>
    <text class="claim" x="925" y="764" font-size="13" letter-spacing="6.5" text-anchor="middle">MIT HANDWERK ZUM ZUHAUSE</text>
    <text class="contact" x="925" y="822" font-size="30" text-anchor="middle">0171/20XX5XX</text>
    <text class="contact" x="925" y="935" font-size="17" text-anchor="middle">www.kalmoranbau-brendel.de</text>
    <text class="contact" x="925" y="958" font-size="11" text-anchor="middle">info@kalmoranbau-brendel.de</text>
  </g>
</svg>
</body>
</html>
```